Business card (AI file uploaded)

We need a business card design that is minimalist using existing logo (attached). Source files must be editable so we can make the same design with other names.

Screenshots included of a design I was working on to give you an idea of the style I would like. Looking for similar modern styles

Thanks

```html
<!DOCTYPE html>
<html lang="en">
<head>
<meta charset="utf-8">
<title>Marlow Law Group – Business Card</title>
<link rel="stylesheet" href="https://fonts.googleapis.com/css2?family=Open+Sans:wght@400;500&display=swap">
<style>
  :root {
    --paper: #ffffff;
    --card: #eef0f0;
    --ink: #1f1f1f;
    --dark-band: #242424;
    --grey-band: #6b6e6e;
    --bleed-line: #c24fc9;
    --safe-line: #7fe0d6;
    --trim-line: #111111;
    --crop-mark: #333333;
    --light-text: #ffffff;
  }
  html, body {
    margin: 0;
    padding: 0;
    width: 863px;
    height: 1200px;
    overflow: hidden;
    background: var(--paper);
  }
  .sheet {
    position: relative;
    width: 863px;
    height: 1200px;
    font-family: "Open Sans", Arial, sans-serif;
    color: var(--ink);
  }
  .sheet-art {
    position: absolute;
    inset: 0;
  }
  .text {
    position: absolute;
    margin: 0;
    white-space: nowrap;
    line-height: 1;
  }
  .firm-name {
    left: 172px;
    top: 140px;
    font-size: 66px;
    font-weight: 400;
    letter-spacing: 0.5px;
  }
  .firm-name .firm-sub {
    display: block;
    font-size: 35px;
    letter-spacing: 6.5px;
    margin-top: 4px;
  }
  .firm-name .firm-suffix {
    font-size: 9px;
    letter-spacing: 1px;
    vertical-align: -6px;
  }
  .person-name {
    left: 173px;
    top: 276px;
    font-size: 36px;
    font-weight: 500;
  }
  .person-title {
    left: 189px;
    top: 326px;
    font-size: 24px;
  }
  .practice-areas {
    left: 175px;
    top: 415px;
    font-size: 19.5px;
    color: var(--light-text);
    word-spacing: 1px;
  }
  .practice-areas .divider {
    margin: 0 9px;
  }
  .contact {
    left: 175px;
    font-size: 22px;
  }
  .contact-address { top: 850px; }
  .contact-phones { top: 897px; }
  .contact-phones .fax { margin-left: 30px; }
  .contact-email { top: 940px; }
</style>
</head>
<body>
<main class="sheet">
  <svg class="sheet-art" width="863" height="1200" viewBox="0 0 863 1200" aria-hidden="true">
    <!-- front card -->
    <g class="card-front">
      <rect x="88" y="80" width="699" height="418" fill="var(--card)"/>
      <path class="grey-swoosh" d="M300,396 C520,375 690,300 787,195 L787,270 C640,350 460,392 300,398 Z" fill="var(--grey-band)"/>
      <path class="dark-swoosh" d="M88,408 C200,406 240,404 300,398 C460,392 640,350 787,270 L787,498 L88,498 Z" fill="var(--dark-band)"/>
      <circle class="firm-mark" cx="583" cy="192" r="47" fill="none" stroke="var(--ink)" stroke-width="4"/>
      <rect class="bleed-line" x="88" y="80" width="699" height="418" fill="none" stroke="var(--bleed-line)" stroke-width="2"/>
      <rect class="trim-line" x="110" y="102" width="655" height="373" fill="none" stroke="var(--trim-line)" stroke-width="2"/>
      <rect class="safe-line" x="134" y="126" width="606" height="325" fill="none" stroke="var(--safe-line)" stroke-width="2"/>
    </g>
    <!-- back card -->
    <g class="card-back">
      <rect x="88" y="713" width="699" height="419" fill="var(--card)"/>
      <rect class="bleed-line" x="88" y="713" width="699" height="419" fill="none" stroke="var(--bleed-line)" stroke-width="2"/>
      <rect class="trim-line" x="110" y="736" width="655" height="374" fill="none" stroke="var(--trim-line)" stroke-width="2"/>
      <rect class="safe-line" x="134" y="760" width="606" height="325" fill="none" stroke="var(--safe-line)" stroke-width="2"/>
    </g>
    <!-- crop marks -->
    <g class="crop-marks" stroke="var(--crop-mark)" stroke-width="1">
      <line x1="110" y1="22" x2="110" y2="62"/><line x1="765" y1="22" x2="765" y2="62"/>
      <line x1="110" y1="510" x2="110" y2="546"/><line x1="765" y1="510" x2="765" y2="546"/>
      <line x1="30" y1="102" x2="68" y2="102"/><line x1="806" y1="102" x2="845" y2="102"/>
      <line x1="30" y1="475" x2="68" y2="475"/><line x1="806" y1="475" x2="845" y2="475"/>
      <line x1="110" y1="655" x2="110" y2="697"/><line x1="765" y1="640" x2="765" y2="685"/>
      <line x1="110" y1="1150" x2="110" y2="1182"/><line x1="765" y1="1140" x2="765" y2="1182"/>
      <line x1="5" y1="736" x2="45" y2="736"/><line x1="806" y1="736" x2="850" y2="736"/>
      <line x1="30" y1="1110" x2="68" y2="1110"/><line x1="806" y1="1110" x2="845" y2="1110"/>
    </g>
  </svg>

  <h1 class="text firm-name">MARLOW<span class="firm-sub">LAW GROUP<span class="firm-suffix">PC</span></span></h1>
  <p class="text person-name">Daniel Marlow</p>
  <p class="text person-title">Attorney At Law</p>
  <p class="text practice-areas">Real Estate<span class="divider">|</span>Bankruptcy<span class="divider">|</span>Social Security Disability</p>

  <p class="text contact contact-address">415 Lakeview Pkwy., Suite 300, Westbrook, IL 60999</p>
  <p class="text contact contact-phones">P: 630.555.0148<span class="fax">F: 630.555.0192</span></p>
  <p class="text contact contact-email">marlow@marlowlaw.com</p>
</main>
</body>
</html>
```